Brightstone Roofing Business Card

This is my current business card. But I’d like to make some changes. Somewhere on the card I’d like to list some of the services we offer. Maybe on the back? But I’d still like to keep the red. White and black modern look.

-residential & commercial roofing
-Roof Repairs & Maintenance
-Storm Damage & Insurance Claims specialist
-Christmas Lights and permanent Christmas lights
Fencing. Windows. Gutters. Siding. Sheetrock, painting.

```html
<!DOCTYPE html>
<html lang="en">
<head>
<meta charset="utf-8">
<title>Brightstone Roofing Business Card</title>
<link rel="stylesheet" href="https://fonts.googleapis.com/css2?family=Audiowide&family=Questrial&family=Ubuntu:wght@400&display=swap">
<style>
  :root {
    --page: #ffffff;
    --ink: #000000;
    --white: #ffffff;
    --red: #d92027;
    --red-deep: #7a0f12;
    --red-dark: #5a0a0c;
    --line: #e6e6e6;
  }
  * { margin: 0; padding: 0; box-sizing: border-box; }
  html, body {
    width: 1100px; height: 1200px; overflow: hidden;
    background: var(--page);
  }
  .sheet { position: relative; width: 1100px; height: 1200px; }

  .card {
    position: absolute; left: 129px; width: 847px; height: 462px;
    border-radius: 30px; overflow: hidden;
  }
  .card--front { top: 94px; }
  .card--back { top: 649px; background: var(--ink); }

  .tartan-field {
    position: absolute; inset: 0;
    background:
      linear-gradient(180deg, rgba(0,0,0,0) 0%, rgba(0,0,0,0) 42%, rgba(0,0,0,0.55) 45%, rgba(0,0,0,0.55) 66%, rgba(0,0,0,0) 69%),
      linear-gradient(135deg, var(--red) 0%, var(--red-deep) 50%, var(--red) 100%);
  }

  .front-name {
    position: absolute; left: 0; right: 0; top: 175px;
    text-align: center; color: var(--white);
    font-family: "Audiowide", sans-serif; font-size: 44px; line-height: 56px;
    letter-spacing: 1px;
  }

  .brand-mark {
    position: absolute; left: 143px; top: 50px;
    width: 90px; height: 90px; border-radius: 50%; background: var(--red);
  }
  .brand-name {
    position: absolute; left: 28px; width: 320px; top: 158px;
    text-align: center; color: var(--white);
    font-family: "Audiowide", sans-serif; font-size: 21px; line-height: 28px;
  }

  .services {
    position: absolute; left: 354px; top: 106px;
    list-style: none; color: var(--white);
    font-family: "Questrial", sans-serif; font-size: 16.5px; line-height: 27.2px;
  }

  .person {
    position: absolute; left: 40px; width: 260px; top: 318px; text-align: right;
  }
  .person-name {
    font-family: "Audiowide", sans-serif; font-size: 24px; color: var(--white);
    letter-spacing: 0.5px; white-space: nowrap;
  }
  .person-name .first { color: var(--red); }
  .person-role {
    margin-top: 4px; font-family: "Ubuntu", sans-serif; font-size: 14px; color: var(--white);
  }
  .person-role em { font-style: normal; color: var(--red); }

  .divider {
    position: absolute; left: 324px; top: 321px; width: 1.5px; height: 68px; background: var(--line);
  }

  .contacts {
    position: absolute; left: 345px; top: 318px; list-style: none;
    font-family: "Ubuntu", sans-serif; font-size: 15px; color: var(--white);
  }
  .contacts li { display: flex; align-items: center; height: 25px; letter-spacing: 0.6px; }
  .contacts li.phone { letter-spacing: 2.5px; }
  .contacts svg { width: 13px; height: 13px; margin-right: 7px; flex: none; }

  .tartan-strip {
    position: absolute; left: 0; right: 0; bottom: 0; height: 18px;
    background: linear-gradient(90deg, var(--red-deep), var(--red) 30%, var(--red-dark) 55%, var(--red) 80%, var(--red-deep));
  }
</style>
</head>
<body>
<main class="sheet">

  <section class="card card--front">
    <div class="tartan-field" role="img" aria-label="Red, black and white tartan plaid background"></div>
    <p class="front-name">BRIGHTSTONE<br>ROOFING CO.</p>
  </section>

  <section class="card card--back">
    <div class="brand-mark"></div>
    <p class="brand-name">BRIGHTSTONE<br>ROOFING CO.</p>

    <ul class="services">
      <li>-residential &amp; commercial roofing</li>
      <li>-Roof Repairs &amp; Maintenance</li>
      <li>-Storm Damage &amp; Insurance Claims specialist</li>
      <li>-Christmas Lights and permanent Christmas lights</li>
      <li>Fencing. Windows. Gutters. Siding. Sheetrock, painting.</li>
    </ul>

    <div class="person">
      <p class="person-name"><span class="first">REID</span> CALLOWAY</p>
      <p class="person-role">Roofing contractor in <em>Texas</em></p>
    </div>

    <div class="divider"></div>

    <ul class="contacts">
      <li class="phone">
        <svg viewBox="0 0 24 24" aria-hidden="true"><path fill="#d92027" d="M6.6 10.8a15.1 15.1 0 0 0 6.6 6.6l2.2-2.2c.3-.3.7-.4 1-.2 1.1.4 2.3.6 3.6.6.6 0 1 .4 1 1V20c0 .6-.4 1-1 1C10.6 21 3 13.4 3 4c0-.6.4-1 1-1h3.5c.6 0 1 .4 1 1 0 1.3.2 2.5.6 3.6.1.3 0 .7-.2 1z"/></svg>
        682-555-0148
      </li>
      <li>
        <svg viewBox="0 0 24 24" aria-hidden="true"><path fill="#d92027" d="M2 5h20v14H2z"/><path fill="none" stroke="#000" stroke-width="1.6" d="M2 5l10 8 10-8M2 19l7-7M22 19l-7-7"/></svg>
        Reid@brightstoneroofing.co
      </li>
      <li>
        <svg viewBox="0 0 24 24" aria-hidden="true"><g fill="none" stroke="#d92027" stroke-width="2"><circle cx="12" cy="12" r="9.5"/><ellipse cx="12" cy="12" rx="4" ry="9.5"/><path d="M2.5 12h19M4 7h16M4 17h16"/></g></svg>
        www.brightstoneroofing.co
      </li>
    </ul>

    <div class="tartan-strip" role="img" aria-label="Thin red and black tartan plaid band"></div>
  </section>

</main>
</body>
</html>
```